Dental Office Looking for Modern, simple business cards

We just acquired our logo. Now we would like to make business cards. We are a dental office with two doctors. We are husband and wife and have a small boutique dental practice in a small town. We love our patients and they are always asking us to give our business cards to their friends. Please help us make business cards :-)

Target Market(s)

30-60 yr old

Industry/Entity Type

Dental Clinic

Contact Information for Business Card

Birch Hollow Dental P.C.
Family and Cosmetic Dentistry
4826 Delmore Rd. Schenectady NY 12417
Tel: 518 642 7731 Fax: 518 642 7048

Dr. Tomas K. Brellin DDS
Dr. Marisol Ede Thornquist DDS

Font styles to use
Serif
Sans Serif

Requirements
Must have
• Simple clean design, modern, colorful. Should incorporate the logo.
Nice to have
• dental imagery ( teeth, smile, etc ...).

```html
<!DOCTYPE html>
<html lang="en">
<head>
<meta charset="utf-8">
<title>Birch Hollow Dental – Business Cards</title>
<link href="https://fonts.googleapis.com/css2?family=Open+Sans:wght@400;600;700&display=swap" rel="stylesheet">
<style>
  :root {
    --backdrop: #d4d4d4;
    --card-white: #ffffff;
    --brand-blue: #1a66b3;
    --card-blue: #1075c0;
    --text-grey: #555a5f;
    --soft-grey: #7a7f84;
  }
  * { margin: 0; padding: 0; box-sizing: border-box; }
  html, body { width: 1200px; height: 802px; overflow: hidden; }
  body {
    background: var(--backdrop);
    font-family: "Open Sans", Arial, sans-serif;
    position: relative;
  }
  .card {
    position: absolute;
    top: 274px;
    width: 442px;
    height: 265px;
    border-radius: 16px;
    box-shadow: 3px 4px 6px rgba(0,0,0,0.35);
  }
  .card-front { left: 136px; background: var(--card-white); }
  .card-back { left: 624px; background: var(--card-blue); }

  .doctors {
    position: absolute;
    left: 24px;
    top: 33px;
    font-size: 14px;
    font-weight: 700;
    line-height: 18px;
    color: var(--brand-blue);
    text-transform: uppercase;
  }
  .doctors .degree { color: var(--soft-grey); font-weight: 600; }

  .brand-name {
    font-weight: 600;
    text-transform: uppercase;
    letter-spacing: 1px;
    white-space: nowrap;
  }
  .card-front .brand-name {
    position: absolute;
    right: 21px;
    top: 104px;
    font-size: 21px;
    color: var(--brand-blue);
  }
  .card-back .brand-name {
    position: absolute;
    left: 0; right: 0;
    top: 118px;
    text-align: center;
    font-size: 25px;
    color: var(--card-white);
  }

  .contact-lines {
    position: absolute;
    left: 24px;
    top: 207px;
    font-size: 11.5px;
    line-height: 16px;
    color: var(--text-grey);
  }
  .contact-lines li { list-style: none; display: flex; align-items: center; gap: 5px; }
  .contact-lines svg { width: 13px; height: 12px; fill: var(--brand-blue); }

  .practice-address {
    position: absolute;
    right: 21px;
    top: 184px;
    text-align: right;
    font-style: normal;
    font-size: 11.5px;
    line-height: 16px;
    color: var(--text-grey);
  }
  .practice-address .practice-name,
  .practice-address .practice-tagline { color: var(--brand-blue); font-weight: 600; }
</style>
</head>
<body>
  <section class="card card-front" aria-label="Business card front">
    <div class="doctors">
      <p>Dr. Tomas K. Brellin <span class="degree">DDS</span></p>
      <p>Dr. Marisol Ede Thornquist <span class="degree">DDS</span></p>
    </div>

    <p class="brand-name">Birch Hollow Dental</p>

    <ul class="contact-lines">
      <li>
        <svg viewBox="0 0 13 12" aria-label="Telephone"><path d="M1 4c0-2 2-3 5.5-3S12 2 12 4l-2.5 1-1-1.5h-4L3.5 5zM3 6h7l2 5H1z"/></svg>
        518 642 7731
      </li>
      <li>
        <svg viewBox="0 0 13 12" aria-label="Fax"><path d="M3 0h7v3H3zM0 4h13v5h-2V7H2v2H0zM3 8h7v4H3z"/></svg>
        518 642 7048
      </li>
    </ul>

    <address class="practice-address">
      <p class="practice-name">Birch Hollow Dental P.C.</p>
      <p class="practice-tagline">Family and Cosmetic Dentistry</p>
      <p>4826 Delmore Rd.</p>
      <p>Schenectady, NY 12417</p>
    </address>
  </section>

  <section class="card card-back" aria-label="Business card back">
    <p class="brand-name">Birch Hollow Dental</p>
  </section>
</body>
</html>
```